Home Inspection Flyer

Looking to have flyer designed that features our business, services, and our contact information. There are three of us. We are all business partners and do not have a company phone number. So each of us would need to be listed on flyer along with our individual phone number. Everything you could possibly need is on our website from logo to services and contact information. https://cedarlinehomereview.com/. If you could possible incorporate our company colors that would be great. You can find those in our logo top left hand side of website and attached. Please also include our homechekguild and nrva logos ( home inspector affiliations ) on brochure as well. Those can be found on website. Please feel free to reach out with any questions.
Thanks
Dale
Updates
Looking to get a few tri fold designs. All the ones submitted have been 8x11

```html
<!DOCTYPE html>
<html lang="en">
<head>
<meta charset="utf-8">
<title>Cedarline Home Review Flyer</title>
<link href="https://fonts.googleapis.com/css2?family=Montserrat:wght@600;700;800&family=Open+Sans:wght@400;600;700&display=swap" rel="stylesheet">
<style>
:root{
  --green:#8cc63f;
  --green-dark:#6fa52a;
  --charcoal:#3b3b3d;
  --ink:#2b2b2b;
  --muted:#666;
  --paper:#ffffff;
  --stage:#e9e9e9;
  --rule:#dcdcdc;
}
*{box-sizing:border-box;margin:0;padding:0}
html,body{width:1200px;height:2192px;overflow:hidden;background:var(--stage)}
body{font-family:"Open Sans",Arial,sans-serif;color:var(--ink)}
.flyer{position:absolute;left:20px;top:296px;width:1160px;height:1600px;background:var(--paper);overflow:hidden;box-shadow:0 6px 24px rgba(0,0,0,.15)}
.header-shapes{position:absolute;left:0;top:0}
.hero-photo{position:absolute;left:470px;top:0;width:690px;height:470px;
  background:linear-gradient(160deg,#b8d4ea 0%,#e8e3d6 45%,#a88d6c 80%,#6b5a45 100%);
  clip-path:polygon(70px 0,100% 0,100% 100%,0 100%)}
.brand{position:absolute;left:40px;top:30px;display:flex;align-items:center;gap:12px}
.brand-mark{width:22px;height:22px;background:var(--green)}
.brand-name{font-family:"Montserrat",sans-serif;font-weight:800;font-size:30px;color:var(--charcoal);letter-spacing:1px}
.hero-copy{position:absolute;left:40px;top:170px;width:400px}
.hero-title{font-family:"Montserrat",sans-serif;font-weight:800;font-size:54px;line-height:1.1;color:#fff}
.hero-sub{margin-top:26px;font-family:"Montserrat",sans-serif;font-weight:700;font-size:22px;line-height:1.35;color:var(--green)}
.col-left{position:absolute;left:40px;top:500px;width:520px}
.col-right{position:absolute;left:610px;top:500px;width:510px}
h2{font-family:"Montserrat",sans-serif;font-weight:800;font-size:24px;line-height:1.25;color:var(--ink)}
p.body{margin-top:14px;font-size:14px;line-height:1.6;color:var(--muted)}
.features{display:flex;gap:40px;margin-top:24px}
.feature{display:flex;flex-direction:column;align-items:center;gap:8px;font-weight:700;font-size:15px}
.icon{width:48px;height:48px;border-radius:8px;background:var(--green);display:flex;align-items:center;justify-content:center}
.contact-bar{margin-top:30px;width:240px;background:var(--green);color:#fff;font-family:"Montserrat",sans-serif;font-weight:800;font-size:20px;padding:10px 18px}
.contact{display:flex;gap:20px;margin-top:22px;align-items:flex-start}
.portrait{width:96px;height:96px;background:linear-gradient(180deg,#6e6e70,#2f2f31);flex:none}
.contact-name{font-family:"Montserrat",sans-serif;font-weight:700;font-size:20px;color:var(--green-dark)}
.contact-role{font-size:13px;color:var(--muted);line-height:1.4;width:240px}
.contact-line{display:flex;align-items:center;gap:8px;font-size:14px;margin-top:6px}
.services{display:grid;grid-template-columns:1fr 1fr;gap:22px 20px;margin-top:28px}
.service{display:flex;flex-direction:column;gap:8px;font-weight:700;font-size:16px}
.service .icon{width:44px;height:44px}
.rule{height:1px;background:var(--rule);margin:34px 0 26px}
.credentials{display:flex;align-items:center;gap:16px;margin-top:22px}
.badge{width:70px;height:70px;border-radius:50%;background:#d8b04a;border:4px solid #f1e3b0}
.badge.alt{background:#9a9a9a;border-color:#dedede}
.site{font-weight:700;font-size:15px;color:var(--green-dark)}
.bottom-strip{position:absolute;left:0;bottom:0}
</style>
</head>
<body>
<main class="flyer">
  <svg class="header-shapes" width="1160" height="470" viewBox="0 0 1160 470">
    <polygon points="0,120 520,120 470,470 0,470" fill="#3b3b3d"/>
    <polygon points="500,0 560,0 490,470 430,470" fill="#8cc63f"/>
  </svg>
  <div class="hero-photo" role="img" aria-label="Photo of a house exterior seen through a magnifying glass held by a hand"></div>
  <div class="brand"><span class="brand-mark"></span><span class="brand-name">CEDARLINE</span></div>
  <div class="hero-copy">
    <h1 class="hero-title">Fast, Affordable, Reliable</h1>
    <p class="hero-sub">For Homeowners, Buyers, Sellers, FSBOs And Real Estate</p>
  </div>

  <section class="col-left">
    <h2>What Is A Cedarline Home Review Buyer Inspection?</h2>
    <p class="body">A home buyer inspection is a visual examination of a home and its systems: interior, plumbing, electrical, roof, attic, foundation, heating and cooling. It gives you a clear picture of the condition of the property before you commit. Our report lists findings with photos and plain notes, so you can decide with confidence, talk with the seller, and plan repairs for the years ahead.</p>
    <div class="features">
      <div class="feature"><span class="icon"><svg width="26" height="26" viewBox="0 0 24 24"><path d="M3 11l9-8 9 8v10h-6v-6H9v6H3z" fill="#fff"/></svg></span>Full Access</div>
      <div class="feature"><span class="icon"><svg width="26" height="26" viewBox="0 0 24 24"><path d="M12 2l8 3v6c0 5-3.5 9-8 11-4.5-2-8-6-8-11V5z" fill="#fff"/></svg></span>Fully Insured</div>
      <div class="feature"><span class="icon"><svg width="26" height="26" viewBox="0 0 24 24"><path d="M6 2h9l4 4v16H6z" fill="#fff"/></svg></span>E2 Report</div>
    </div>
    <div class="contact-bar">CONTACT US</div>
    <div class="contact">
      <div class="portrait" role="img" aria-label="Portrait of Warren Tolle"></div>
      <div><div class="contact-name">Warren Tolle</div><div class="contact-role">Certified Home Inspector and Building Consultant</div>
        <div class="contact-line"><svg width="14" height="14" viewBox="0 0 24 24"><path d="M6 2l4 4-2 3c1 3 4 6 7 7l3-2 4 4-3 4C10 21 3 14 2 5z" fill="#8cc63f"/></svg>(724) 555-0148</div>
        <div class="contact-line"><svg width="14" height="14" viewBox="0 0 24 24"><rect x="2" y="5" width="20" height="14" fill="#8cc63f"/></svg>warren@cedarlinehome.com</div></div>
    </div>
    <div class="contact">
      <div class="portrait" role="img" aria-label="Portrait of Jesse Marlow"></div>
      <div><div class="contact-name">Jesse Marlow</div><div class="contact-role">Certified Home Inspector and Building Consultant</div>
        <div class="contact-line"><svg width="14" height="14" viewBox="0 0 24 24"><path d="M6 2l4 4-2 3c1 3 4 6 7 7l3-2 4 4-3 4C10 21 3 14 2 5z" fill="#8cc63f"/></svg>(412) 555-0172</div>
        <div class="contact-line"><svg width="14" height="14" viewBox="0 0 24 24"><rect x="2" y="5" width="20" height="14" fill="#8cc63f"/></svg>jesse@cedarlinehome.com</div></div>
    </div>
    <div class="contact">
      <div class="portrait" role="img" aria-label="Portrait of Dale Hessel"></div>
      <div><div class="contact-name">Dale Hessel</div><div class="contact-role">Certified Home Inspector and Building Consultant</div>
        <div class="contact-line"><svg width="14" height="14" viewBox="0 0 24 24"><path d="M6 2l4 4-2 3c1 3 4 6 7 7l3-2 4 4-3 4C10 21 3 14 2 5z" fill="#8cc63f"/></svg>(412) 555-0193</div>
        <div class="contact-line"><svg width="14" height="14" viewBox="0 0 24 24"><rect x="2" y="5" width="20" height="14" fill="#8cc63f"/></svg>dale@cedarlinehome.com</div></div>
    </div>
  </section>

  <section class="col-right">
    <h2>Cedarline Home Review Inspection Services</h2>
    <p class="body">Select an inspection or testing service for more information.</p>
    <div class="services">
      <div class="service"><span class="icon"><svg width="24" height="24" viewBox="0 0 24 24"><path d="M3 11l9-8 9 8v10H3z" fill="#fff"/></svg></span>Home Inspection</div>
      <div class="service"><span class="icon"><svg width="24" height="24" viewBox="0 0 24 24"><path d="M12 2c4 6 6 9 6 12a6 6 0 0 1-12 0c0-3 2-6 6-12z" fill="#fff"/></svg></span>Water Sample Test</div>
      <div class="service"><span class="icon"><svg width="24" height="24" viewBox="0 0 24 24"><circle cx="12" cy="13" r="6" fill="#fff"/></svg></span>Pest Inspection</div>
      <div class="service"><span class="icon"><svg width="24" height="24" viewBox="0 0 24 24"><rect x="7" y="3" width="10" height="18" fill="#fff"/></svg></span>Well Flow Test</div>
      <div class="service"><span class="icon"><svg width="24" height="24" viewBox="0 0 24 24"><circle cx="12" cy="12" r="8" fill="none" stroke="#fff" stroke-width="3"/></svg></span>Radon Inspection</div>
      <div class="service"><span class="icon"><svg width="24" height="24" viewBox="0 0 24 24"><rect x="3" y="8" width="18" height="10" fill="#fff"/></svg></span>Septic Dye Flow Test</div>
      <div class="service"><span class="icon"><svg width="24" height="24" viewBox="0 0 24 24"><rect x="3" y="7" width="13" height="10" fill="#fff"/><path d="M16 10l5-3v10l-5-3z" fill="#fff"/></svg></span>Sewer Camera Inspection</div>
    </div>
    <div class="rule"></div>
    <h2>OVER 10 YEARS OF HOME INSPECTION EXPERIENCE</h2>
    <p class="body">We've inspected thousands of homes around Pittsburgh and the surrounding areas. At Cedarline we serve residents of Southwestern PA and beyond with an unwavering commitment to excellence.</p>
    <div class="credentials">
      <span class="badge" role="img" aria-label="NRVA member badge"></span>
      <span class="badge alt" role="img" aria-label="HomeChekGuild member badge"></span>
      <span class="site">https://cedarlinehomereview.com/</span>
    </div>
  </section>

  <svg class="bottom-strip" width="1160" height="40" viewBox="0 0 1160 40">
    <rect x="0" y="22" width="1160" height="18" fill="#3b3b3d"/>
    <polygon points="760,40 800,0 1160,0 1160,40" fill="#8cc63f"/>
  </svg>
</main>
</body>
</html>
```